13 Tavo - new website design project

Our company Tavo Electrical is developing a new lead generation website focused on Electrical, LED Lighting and Solar Power. We need a high converting website.

Example of our current website is www.tavoelectrical.com.au You can take content from this website for this new design. Our colours are red, black and white. For our new website we would like to promote Tavo, Bright Days Ahead. Please listen to the jingle.

The below link is the company jingle that we have developed.
http://www.tunecraftaudio.com.au/tav-tc-v1/

The key for this brief is to generate leads for Electrical, LED Lighting (for commercial) and Solar Power & Storage.

Target Market(s)

Business owners in Melbourne Victoria

Number of Pages Required

4 page

Colors
ec1f27
ffffff

Requirements
Must have
• This page must be clean, be in line with company branding and a high converting lead website.

```html
<!DOCTYPE html>
<html lang="en">
<head>
<meta charset="utf-8">
<title>Tavo Electrical</title>
<link rel="stylesheet" href="https://fonts.googleapis.com/css2?family=Cinzel:wght@700&family=Roboto+Condensed:ital,wght@1,700&family=Open+Sans:wght@400;600;700&display=swap">
<style>
:root{
  --red:#ec1f27;
  --red-deep:#c8161d;
  --white:#ffffff;
  --ink:#1e1e1e;
  --grey-text:#555555;
  --dark:#3a3a3a;
  --darker:#2a2a2a;
  --brick:#2c2c2c;
  --line:#d8d8d8;
}
*{box-sizing:border-box;margin:0;padding:0}
html,body{width:1200px;height:3492px;overflow:hidden}
body{position:relative;font-family:"Open Sans",Arial,sans-serif;color:var(--ink);background:var(--white)}
.section{position:absolute;left:0;width:1200px}
.section-title{font-family:"Cinzel",Georgia,serif;font-weight:700;color:var(--red);font-size:46px;letter-spacing:1px}
.btn{display:inline-block;background:var(--darker);color:var(--white);font-size:17px;font-weight:600;padding:16px 30px;border-radius:30px;text-transform:uppercase}
.btn-light{background:var(--white);color:var(--ink)}

/* hero */
.hero{top:0;height:680px;background:linear-gradient(180deg,#e9eaec 0%,#cfd1d4 45%,#9a9da2 100%)}
.hero-photo{position:absolute;inset:0;background:radial-gradient(ellipse at 62% 45%,#b89578 0%,#8e8a86 30%,rgba(200,202,205,0) 60%),linear-gradient(180deg,#eceef0,#b7babe)}
.top-nav{position:absolute;top:0;left:0;width:1200px;height:84px;display:flex;align-items:center}
.brand{margin-left:40px;display:flex;align-items:center;gap:12px}
.brand-dot{width:40px;height:40px;border-radius:50%;background:var(--red)}
.brand-name{font-family:"Open Sans",sans-serif;font-weight:700;font-size:34px;color:var(--white)}
.nav-links{margin-left:auto;display:flex;gap:34px;font-size:17px;color:var(--white);font-weight:600;margin-right:30px}
.nav-links .active{color:var(--red)}
.nav-phone{margin-right:40px;color:var(--red);font-weight:700;font-size:26px}
.hero-headline{position:absolute;left:40px;top:370px;font-family:"Roboto Condensed",sans-serif;font-style:italic;font-weight:700;font-size:54px;color:var(--red);text-transform:uppercase;text-shadow:0 2px 2px rgba(0,0,0,.25)}
.hero-sub{position:absolute;left:40px;top:432px;width:600px;font-size:26px;font-weight:600;color:var(--ink);line-height:1.3}
.hero .btn{position:absolute;left:72px;top:524px}

/* about */
.about{top:680px;height:340px;background:var(--white)}
.about .section-title{position:absolute;left:72px;top:44px}
.about-rule{position:absolute;left:72px;top:110px;width:700px;height:2px;background:var(--line)}
.about-text{position:absolute;left:72px;top:124px;width:690px;font-size:14px;line-height:1.4;color:var(--grey-text)}
.about-photo{position:absolute;left:790px;top:96px;width:330px;height:176px;background:linear-gradient(135deg,#6a6d72,#2f3136)}
.about .btn{position:absolute;left:72px;top:270px;padding:14px 28px;font-size:15px}

/* services */
.services{top:1020px;height:580px;background:repeating-linear-gradient(0deg,#262626 0 38px,#1a1a1a 38px 40px),var(--brick)}
.services .section-title{position:absolute;width:100%;text-align:center;top:42px}
.services-intro{position:absolute;left:240px;top:138px;width:720px;text-align:center;color:#cfcfcf;font-size:14px;line-height:1.4}
.service{position:absolute;top:236px;width:260px;text-align:center}
.service-photo{width:260px;height:260px;border-radius:50%;border:5px solid var(--white)}
.service-label{margin:14px auto 0;width:220px;background:var(--darker);color:var(--white);font-size:17px;font-weight:600;padding:6px 0;border-bottom:3px solid var(--red);text-transform:uppercase}

/* why */
.why{top:1600px;height:620px}
.why-panel{position:absolute;left:0;top:0;width:600px;height:620px;background:var(--red)}
.why .section-title{position:absolute;left:0;width:600px;text-align:center;top:78px;color:var(--white)}
.why-mark{position:absolute;left:230px;top:170px;width:140px;height:140px;border-radius:50%;background:var(--white);display:flex;align-items:center;justify-content:center;font-weight:700;font-size:34px;color:var(--red)}
.why-text{position:absolute;left:120px;top:330px;width:360px;text-align:center;color:var(--white);font-size:14px;line-height:1.45}
.why .btn{position:absolute;left:240px;top:540px;padding:13px 28px;font-size:15px}
.reasons{position:absolute;left:630px;top:70px;width:520px;list-style:none}
.reason{position:relative;height:120px;padding-left:80px}
.reason-num{position:absolute;left:0;top:6px;width:56px;height:56px;border-radius:50%;background:var(--red);color:var(--white);font-size:24px;font-weight:700;display:flex;align-items:center;justify-content:center}
.reason h3{font-size:30px;font-weight:400;color:var(--ink);line-height:1.1}
.reason p{font-size:13px;color:var(--grey-text);line-height:1.35;margin-top:4px}

/* partners */
.partners{top:2220px;height:200px;background:var(--white);display:flex;justify-content:space-around;align-items:center;padding:0 50px}
.partner{width:180px;height:110px}

/* blog */
.blog{top:2420px;height:520px;background:linear-gradient(180deg,#f3f3f3,#ffffff)}
.blog .section-title{position:absolute;width:100%;text-align:center;top:38px;color:var(--ink)}
.post{position:absolute;top:120px;width:264px}
.post-photo{width:264px;height:130px}
.post h4{margin-top:10px;font-size:18px;font-weight:400;color:var(--red)}
.post-date{font-size:12px;color:var(--grey-text);margin-top:4px}
.post p{font-size:13px;color:var(--grey-text);line-height:1.4;margin-top:6px}
.post-more{font-size:13px;font-weight:700;margin-top:10px;color:var(--ink)}

/* contact */
.contact{top:2940px;height:508px;background:var(--dark)}
.contact .section-title{position:absolute;width:100%;text-align:center;top:32px;color:var(--white)}
.contact-intro{position:absolute;left:320px;top:100px;width:560px;text-align:center;color:#dddddd;font-size:14px;line-height:1.4}
.field{position:absolute;height:40px;background:var(--white);font-size:13px;color:#666;padding:11px 12px}
.submit{position:absolute;left:578px;top:432px;width:160px;height:44px;border:2px solid var(--white);color:var(--white);font-size:15px;font-weight:600;text-align:center;line-height:40px}
.contact-info{position:absolute;left:800px;top:156px;width:340px;color:var(--white);font-size:14px}
.contact-info .tagline{font-size:16px;margin-bottom:24px}
.contact-info .tagline b{font-weight:700}
.info-row{display:flex;align-items:center;gap:14px;margin-bottom:26px}
.socials{position:absolute;left:820px;top:424px;display:flex;gap:8px}
.social{width:44px;height:44px;background:var(--darker)}
.social.first{background:var(--red)}

.footer{top:3448px;height:44px;background:var(--darker);color:#cccccc;font-size:13px;text-align:center;line-height:44px}
</style>
</head>
<body>

<header class="section hero">
  <div class="hero-photo" role="img" aria-label="Electrician in a checked shirt fitting a fluorescent light panel in an office ceiling"></div>
  <nav class="top-nav">
    <div class="brand"><span class="brand-dot"></span><span class="brand-name">Tavo</span></div>
    <div class="nav-links"><span class="active">● HOME</span><span>TAVO STORY</span><span>OUR WORK</span><span>CONTACT US</span></div>
    <div class="nav-phone">13 8826</div>
  </nav>
  <h1 class="hero-headline">Electrical, LED Lighting, Solar Power</h1>
  <p class="hero-sub">Auatralia's Largest fully integrated electrical &amp; engry solutions provider.</p>
  <span class="btn">Contact Us Now</span>
</header>

<section class="section about">
  <h2 class="section-title">About Tavo</h2>
  <div class="about-rule"></div>
  <p class="about-text">Lorem Ipsum is simply dummy text of the printing and typesetting industry. Lorem Ipsum has been the industry's standard dummy text ever since the 1500s, when an unknown printer took a galley of type and scrambled it to make a type specimen book. It has survived not only five centuries, but also the leap into electronic typesetting, remaining essentially unchanged. It was popularised in the 1960s with the release of Letraset sheets containing Lorem Ipsum passages.</p>
  <div class="about-photo" role="img" aria-label="Team photo of electricians beside a company van"></div>
  <span class="btn">Read More</span>
</section>

<section class="section services">
  <h2 class="section-title">Our Services</h2>
  <p class="services-intro">Tavo Electrical was formed to be an expert Electrical Contracting Company providing services to its Residential and Commercial Customers. With over 15 years of experience, Tavo Electrical has developed a highly experienced team of professionals that ensure all our customer expectations are met.</p>
  <div class="service" style="left:80px">
    <div class="service-photo" style="background:radial-gradient(circle at 40% 40%,#f2c230,#d8a23a 40%,#e8ecef 75%)" role="img" aria-label="Electrician in a yellow hard hat"></div>
    <div class="service-label">Electrical</div>
  </div>
  <div class="service" style="left:470px">
    <div class="service-photo" style="background:radial-gradient(circle at 50% 60%,#f7d38a,#b4692c 40%,#2b1d14 80%)" role="img" aria-label="Row of glowing LED pendant lights"></div>
    <div class="service-label">LED Lighting</div>
  </div>
  <div class="service" style="left:860px">
    <div class="service-photo" style="background:linear-gradient(135deg,#9fc3e6,#2a4f8a 55%,#c9b8a4)" role="img" aria-label="Technician holding a solar panel"></div>
    <div class="service-label">Solar Power</div>
  </div>
</section>

<section class="section why">
  <div class="why-panel"></div>
  <h2 class="section-title">Why Choose us?</h2>
  <div class="why-mark">Tavo</div>
  <p class="why-text">Lorem Ipsum is simply dummy text of the printing and typesetting industry. Lorem Ipsum has been the industry's standard dummy text ever since the 1500s, when an unknown printer took a galley of type and scrambled it to make a type specimen book. It has survived not only five centuries, but also the leap into electronic typesetting, remaining essentially unchanged.</p>
  <span class="btn btn-light">Read More</span>
  <ol class="reasons">
    <li class="reason"><span class="reason-num">1</span><h3>Professional service</h3><p>When you hire a Tavo Electrical Electrician you will get a professional and well organised Electrician that comes skilled and ready to do the job.</p></li>
    <li class="reason"><span class="reason-num">2</span><h3>5 year wormanship guarantee</h3><p>You can buy with confidence as all of our work has a 5 year workmanship guarantee. For your peace of mind, we back our work.</p></li>
    <li class="reason"><span class="reason-num">3</span><h3>Value for Money</h3><p>We provide extremely competitive pricing, which means you get value for money on quality that is comparable to the best in the industry.</p></li>
    <li class="reason"><span class="reason-num">4</span><h3>Environmentally friendly</h3><p>We're committed to reducing carbon emissions by installing Solar Power and upgrading sites to LED Lighting.</p></li>
    <li class="reason"><span class="reason-num">5</span><h3>Fully insured</h3><p>Tavo Electrical is fully insured and equipped to handle small, medium and large scale jobs.</p></li>
  </ol>
</section>

<section class="section partners">
  <div class="partner" style="background:#e0418f"></div>
  <div class="partner" style="background:#d71920"></div>
  <div class="partner" style="background:#e3262e;border-radius:8px"></div>
  <div class="partner" style="background:#f7d117"></div>
</section>

<section class="section blog">
  <h2 class="section-title">Latest Blog</h2>
  <article class="post" style="left:72px">
    <div class="post-photo" style="background:linear-gradient(135deg,#c7d7e6,#8fa6bb)" role="img" aria-label="Children playing indoors"></div>
    <h4>Lorem Ipsum is simply</h4><div class="post-date">▣ 10 JAN 2017</div>
    <p>Lorem Ipsum is simply dummy text of the printing and typesetting.</p><div class="post-more">KNOW MORE ›</div>
  </article>
  <article class="post" style="left:348px">
    <div class="post-photo" style="background:linear-gradient(180deg,#7fb3e3,#2b4a7a 60%,#6d8a3a)" role="img" aria-label="House roof with solar panels"></div>
    <h4>Lorem Ipsum is simply</h4><div class="post-date">▣ 10 JAN 2017</div>
    <p>Lorem Ipsum is simply dummy text of the printing and typesetting.</p><div class="post-more">KNOW MORE ›</div>
  </article>
  <article class="post" style="left:624px">
    <div class="post-photo" style="background:radial-gradient(circle,#f5e3b3,#6b6b6b 70%)" role="img" aria-label="Modern ceiling light fitting"></div>
    <h4>Lorem Ipsum is simply</h4><div class="post-date">▣ 10 JAN 2017</div>
    <p>Lorem Ipsum is simply dummy text of the printing and typesetting.</p><div class="post-more">KNOW MORE ›</div>
  </article>
  <article class="post" style="left:900px">
    <div class="post-photo" style="background:linear-gradient(135deg,#d9dcdf,#8a9096)" role="img" aria-label="Office interior with LED downlights"></div>
    <h4>Lorem Ipsum is simply</h4><div class="post-date">▣ 10 JAN 2017</div>
    <p>Lorem Ipsum is simply dummy text of the printing and typesetting.</p><div class="post-more">KNOW MORE ›</div>
  </article>
</section>

<section class="section contact">
  <h2 class="section-title">Contact Us Now</h2>
  <p class="contact-intro">Lorem Ipsum is simply dummy text of the printing and typesetting industry. Lorem Ipsum has been the industry's standard dummy text.</p>
  <div class="field" style="left:72px;top:156px;width:320px">Your Name</div>
  <div class="field" style="left:416px;top:156px;width:322px">Your E-Mail</div>
  <div class="field" style="left:72px;top:216px;width:320px">Your Phone</div>
  <div class="field" style="left:416px;top:216px;width:322px">Purpose ▾</div>
  <div class="field" style="left:72px;top:276px;width:666px">Address</div>
  <div class="field" style="left:72px;top:336px;width:666px;height:76px">Message</div>
  <div class="submit">SUBMIT</div>
  <div class="contact-info">
    <p class="tagline"><b>TAVO</b> bright days ahead</p>
    <div class="info-row"><svg width="22" height="28" viewBox="0 0 22 28"><path d="M11 0a10 10 0 0 0-10 10c0 8 10 18 10 18s10-10 10-18A10 10 0 0 0 11 0z" fill="#ffffff"/><circle cx="11" cy="10" r="4" fill="#3a3a3a"/></svg><span>24-86 Harlow St Glen Ashby<br>VIC 3152</span></div>
    <div class="info-row"><svg width="22" height="22" viewBox="0 0 24 24"><path d="M6.6 10.8a15 15 0 0 0 6.6 6.6l2.2-2.2a1 1 0 0 1 1-.25 11.4 11.4 0 0 0 3.6.6 1 1 0 0 1 1 1V20a1 1 0 0 1-1 1A17 17 0 0 1 3 4a1 1 0 0 1 1-1h3.5a1 1 0 0 1 1 1c0 1.25.2 2.45.6 3.6a1 1 0 0 1-.25 1z" fill="#ffffff"/></svg><span>13 8826</span></div>
    <div class="info-row"><svg width="22" height="16" viewBox="0 0 22 16"><rect x="1" y="1" width="20" height="14" fill="none" stroke="#ffffff" stroke-width="2"/><path d="M1 1l10 8 10-8" fill="none" stroke="#ffffff" stroke-width="2"/></svg><span>service@tavoelectrical.com.au</span></div>
  </div>
  <div class="socials"><span class="social first"></span><span class="social"></span><span class="social"></span></div>
</section>

<footer class="section footer">© TAVO ELECTRICAL - 2017. All Rights Reserved.</footer>

</body>
</html>
```